The Nine Gates for Tablet Reliance - Contemporary Book Cover Design

The Nine Gates for Tablet Reliance was published in March 2019 and is available on Brimora and other platforms now. However, I am not happy with the cover.  It's a good design in some ways - I thought it would stand out and be easily recognizable. But I don't really like the color scheme and feel that a self-help book should probably use some lighter colors and that the red is too strident. The color scheme carries over into other marketing materials like the website, social media, etc. and I don't like the red and black scheme for these purposes.
It's not essential that the cover contain an endorsement like the current one but it could. Here are some endorsements:
“A must-read for anyone who is addicted to or thinks they may have a problem with digital technology. This eloquent work will also be useful to academics and clinicians exploring potential solutions. The author recognizes the similarities between smartphone addiction and other addictions, and logically applies one of the most effective known solutions for addiction - The Nine Gates.”
-- Dale Wickersham: Noted Interventionist, Keynote Speaker and Addiction Visionary
“If you suffer from digital addiction, I strongly encourage you to use this book as your road map to get you back to the real world.”
-- Thomas Quillard, Founder of Online Channel Monitor.
The back cover would have the new design / color scheme, but can have similar text, bio, author image, etc. Or we could include the endorsements there and shorten the other text.
As for the cover it could be stylized, or an image, a partial image, or whatever. I am open to suggestions. Think about what would be inviting for a person searching for help with moderating their smartphone use.
Let's add a subtitle as well "An Inner Journey to Balanced Tablet Habits"
Here is a link to the book:
https://www.brimora.example/Nine-Gates-Tablet-Reliance/dp/4086213590

Target Market(s)
General, since this issue affects almost everyone.
Colors
Designer to choose colors to be used in the design.
Look and feel

```html
<!DOCTYPE html>
<html lang="en">
<head>
<meta charset="utf-8">
<title>The Nine Gates for Tablet Reliance – Cover</title>
<link rel="stylesheet" href="https://fonts.googleapis.com/css2?family=Tinos:ital,wght@0,400;1,400&family=Pinyon+Script&display=swap">
<style>
  :root {
    --page-bg: #ffffff;
    --cover-bg: #e2c6ad;
    --ink: #1f1f26;
    --phone-body: #1b1b1f;
    --phone-edge: #3a3a40;
    --screen-top: #d9c3b3;
    --screen-glow: #dca08f;
    --screen-peak: #e9b3a4;
    --screen-ridge: #8a7480;
    --screen-deep: #3a3640;
    --screen-base: #25242a;
    --bubble-line: #e2a69e;
    --title-white: #ffffff;
  }
  * { box-sizing: border-box; margin: 0; padding: 0; }
  html, body {
    width: 1200px; height: 1106px; overflow: hidden;
    background: var(--page-bg);
  }
  .cover {
    position: absolute; left: 253px; top: 33px;
    width: 693px; height: 1040px;
    background: var(--cover-bg);
    font-family: "Tinos", "Times New Roman", serif;
    color: var(--ink);
  }
  .endorsement {
    position: absolute; left: 30px; right: 30px; top: 40px;
    text-align: center; font-style: italic;
    font-size: 23px; line-height: 1.2;
  }
  .endorsement cite { display: block; font-style: italic; }
  .phone {
    position: absolute; left: 78px; top: 150px;
    width: 348px; height: 750px;
    background: var(--phone-body);
    border: 3px solid var(--phone-edge);
    border-radius: 48px;
    padding: 44px 12px 16px;
  }
  .phone-speaker {
    position: absolute; top: 18px; left: 50%;
    width: 56px; height: 6px; margin-left: -28px;
    border-radius: 3px; background: #4a4a52;
  }
  .phone-sensor {
    position: absolute; top: 16px; width: 9px; height: 9px;
    border-radius: 50%; background: #35353c;
  }
  .phone-sensor.left { left: 40px; }
  .phone-sensor.right { right: 46px; }
  .screen {
    position: relative; width: 100%; height: 100%;
    border-radius: 30px; overflow: hidden;
  }
  .screen-scenery {
    position: absolute; inset: 0;
    background: linear-gradient(180deg,
      var(--screen-top) 0%,
      var(--screen-glow) 30%,
      var(--screen-peak) 38%,
      var(--screen-ridge) 52%,
      var(--screen-deep) 72%,
      var(--screen-base) 100%);
  }
  .title {
    position: absolute; left: 0; right: 0; top: 30px;
    color: var(--title-white); text-align: center;
  }
  .title-lead { position: relative; height: 118px; }
  .title-number {
    position: absolute; left: 20px; top: -18px;
    font-family: "Pinyon Script", cursive;
    font-size: 130px; line-height: 1;
  }
  .title-the {
    position: absolute; left: 58px; top: 34px;
    font-size: 17px;
  }
  .title-words {
    position: absolute; left: 140px; top: 2px;
    text-align: left; font-size: 44px; line-height: 1;
  }
  .title-main {
    font-size: 45px; line-height: 1.05; letter-spacing: 0.5px;
  }
  .bubble {
    position: absolute; left: 368px; top: 395px;
    width: 310px; height: 230px;
  }
  .bubble svg { position: absolute; inset: 0; }
  .bubble-text {
    position: absolute; left: 50px; right: 28px; top: 50px;
    text-align: center; font-size: 24px; line-height: 1.25;
  }
  .author {
    position: absolute; left: 0; right: 0; top: 925px;
    text-align: center; font-size: 62px; letter-spacing: -0.5px;
  }
</style>
</head>
<body>
  <main class="cover">
    <blockquote class="endorsement">
      “If you suffer from digital addiction, I strongly encourage you to use this book as your road map to get you back to the real world.”
      <cite>-- Thomas Quillard, Founder of Online Channel Monitor</cite>
    </blockquote>

    <div class="phone">
      <span class="phone-sensor left"></span>
      <span class="phone-speaker"></span>
      <span class="phone-sensor right"></span>
      <div class="screen">
        <div class="screen-scenery" role="img" aria-label="Aerial view of a snowy mountain range glowing pink at sunset"></div>
        <h1 class="title">
          <div class="title-lead">
            <span class="title-number">9</span>
            <span class="title-the">The</span>
            <span class="title-words">Gates<br>for</span>
          </div>
          <div class="title-main">TABLET<br>RELIANCE</div>
        </h1>
      </div>
    </div>

    <div class="bubble">
      <svg viewBox="0 0 310 230" width="310" height="230" aria-hidden="true">
        <path d="M60 150 C20 120 25 45 95 25 C160 5 265 15 290 70 C310 120 265 175 185 180 C140 183 110 180 85 175 L40 215 L55 165 Z"
              fill="var(--cover-bg)" stroke="var(--bubble-line)" stroke-width="10" stroke-linejoin="round"/>
      </svg>
      <p class="bubble-text">An Inner Journey to Balanced Tablet Habits</p>
    </div>

    <p class="author">Jonah Severin</p>
  </main>
</body>
</html>
```